VARSEK MOBILE APP RE-DESIGN - MINIMALISTIC AND CLEAN DESIGN

We are looking for a design that is minimalistic, clean, modern and appealing to millennials...
IMPORTANT: This is NOT a logo design nor a website design... This is for a mobile App Design. You can download our app on iOS or Android: "VARSEK eLINKUP"

We are attaching our new logo and some apps that we like the design, colors, shadows, 3d effects, style, etc...

For content, you can check our website: www.varsek-app.example

Please feel free to ask questions, it's very important that you understand the project. Thank you

Also, check out this website...we do like the design and colors: https://brontil-demo.example/
Updates

This is not for a logo design... this is for a mobile app design.... please download our app on iOS: VARSEK eLINKUP... THANK YOU

Target Market(s)

20 - 35
60% Male 40 Female

Requirements
Must have
• great graphics, color shadows for 3d effects, great colors with transparency, IMPORTANT: CLEAN DESIGN, Minimalistic.

```html
<!DOCTYPE html>
<html lang="en">
<head>
<meta charset="utf-8">
<title>Varsek onboarding screens</title>
<link href="https://fonts.googleapis.com/css2?family=Roboto:wght@400;500;700;900&display=swap" rel="stylesheet">
<style>
:root{
  --stage:#1569b8;
  --screen:#f3f5f8;
  --ink:#2f3640;
  --muted:#6b7380;
  --navy:#1e3a8a;
  --sky:#12a4e0;
  --wash:#d3ebf5;
  --wash-deep:#a9d8ee;
  --bar:#c9ced6;
}
*{box-sizing:border-box;margin:0;padding:0}
html,body{width:1200px;height:1200px;overflow:hidden}
body{background:var(--stage);font-family:"Roboto",sans-serif;position:relative}
.screen{
  position:absolute;width:240px;height:488px;background:var(--screen);
  border-radius:30px;box-shadow:0 18px 40px rgba(5,30,80,.35);overflow:hidden;
}
.home-bar{position:absolute;left:80px;top:466px;width:80px;height:3px;border-radius:2px;background:var(--bar)}
.brand{position:absolute;left:0;right:0;display:flex;align-items:center;justify-content:center;gap:8px;
  font-weight:500;color:var(--ink)}
.brand-dot{border-radius:50%;background:var(--navy)}
.brand--small{top:60px;font-size:20px}
.brand--small .brand-dot{width:18px;height:18px}
.brand--large{top:226px;font-size:27px}
.brand--large .brand-dot{width:26px;height:26px}
.art{position:absolute;left:14px;right:14px;border-radius:18px;
  background:linear-gradient(180deg,var(--wash) 0%,var(--wash-deep) 100%)}
.title{position:absolute;left:0;right:0;text-align:center;top:216px;font-size:11px;font-weight:700;color:var(--ink)}
.title--hero{font-size:19px;font-weight:900;top:210px}
.body-text{position:absolute;left:16px;right:16px;top:242px;text-align:center;font-size:8.4px;line-height:14.5px;color:var(--muted)}
.dots{position:absolute;top:315px;left:0;right:0;display:flex;justify-content:center;gap:10px}
.dot{width:9px;height:9px;border-radius:50%;border:1px solid var(--navy)}
.dot--on{background:var(--navy)}
.button{position:absolute;left:80px;top:372px;width:80px;height:28px;border-radius:14px;
  background:linear-gradient(90deg,var(--navy),var(--sky));color:#fff;font-size:8.5px;font-weight:500;
  display:flex;align-items:center;justify-content:center}
.link{position:absolute;left:0;right:0;top:412px;text-align:center;font-size:8.5px;font-weight:500;color:var(--sky)}
</style>
</head>
<body>

<section class="screen" style="left:82px;top:264px">
  <div class="brand brand--large"><span class="brand-dot"></span>varsek</div>
  <div class="home-bar"></div>
</section>

<section class="screen" style="left:342px;top:42px">
  <div class="brand brand--small"><span class="brand-dot"></span>varsek</div>
  <h1 class="title title--hero">Welcome</h1>
  <p class="body-text">Join us &amp; get tons of rewards by<br>helping others get rewards.</p>
  <div class="button">Get Started</div>
  <div class="home-bar"></div>
</section>

<section class="screen" style="left:606px;top:166px">
  <div class="art" role="img" aria-label="Illustration of two people exchanging rewards" style="top:30px;height:146px"></div>
  <h2 class="title">Earn unlimited, share unlimited</h2>
  <p class="body-text">Upgrade to premium membership<br>to earn unlimited rewards.</p>
  <div class="dots"><span class="dot"></span><span class="dot dot--on"></span><span class="dot"></span></div>
  <div class="button">Next</div>
  <div class="home-bar"></div>
</section>

<section class="screen" style="left:343px;top:554px">
  <div class="art" role="img" aria-label="Illustration of three people around a large phone" style="top:32px;height:172px"></div>
  <h2 class="title">Making referral easy</h2>
  <p class="body-text">Share your referral codes and links<br>to be used by anyone, anywhere, anytime!</p>
  <div class="dots"><span class="dot dot--on"></span><span class="dot"></span><span class="dot"></span></div>
  <div class="button">Next</div>
  <div class="home-bar"></div>
</section>

<section class="screen" style="left:602px;top:679px">
  <div class="art" role="img" aria-label="Illustration of three friends jumping with joy" style="top:34px;height:150px"></div>
  <h2 class="title">More people, more rewards</h2>
  <p class="body-text">Don't forgot to invite<br>your friends and family.</p>
  <div class="dots"><span class="dot"></span><span class="dot"></span><span class="dot dot--on"></span></div>
  <div class="button">Next</div>
  <div class="home-bar"></div>
</section>

<section class="screen" style="left:867px;top:473px">
  <div class="art" role="img" aria-label="Illustration of people beside laptop, tablet and phone screens" style="top:40px;height:150px"></div>
  <h2 class="title title--hero">Okay</h2>
  <p class="body-text">Let's start earning rewards<br>with a FREE account!</p>
  <div class="button">Register</div>
  <div class="link">Later</div>
  <div class="home-bar"></div>
</section>

</body>
</html>
```